Lumo leadership hierchy redesign

Hi there, you created an awesome graphic design a while back. In our martial arts organization, elements are used to indicate an individuals leadership level and authority.
You start with a white uniform (black lumo logos) and earn three different collars like a rising sun....
Purple, then Orange, Then Yellow.
After a student earns yellow collar....they will earn elemental logos on their black belt. We use to do colored collars for the wind, water, fire, and earth leadership levels but now we want to simplfy everything and put a colored hexagonal element logo in their black belt.
So after an individual earns a yellow collar.....
Their next goal is to either become a Program Director (Water) or a Lead Instructor (Wind)
For the Water Element, there are 4 levels you could earn as a logo on your black belt
Level 1 would be a Royal Blue hexagon outlined in white with our water symbol in the middle in white. Also label it with the rules to earn it: 50 Active Students
Level 2 would be a Royal Blue hexagon outlined in black with our water symbol in the middle in black.
Also label it with the rules to earn it: 100 Active Students
Level 3 would be a Royal Blue hexagon outlined in silver with our water symbol in the middle in silver.
Also label it with the rules to earn it: 150 Active Students.
Level 4 would be a Royal Blue hexagon outlined in silver with our water symbol in the middle in silver.
Also label it with the rules to earn it: 200
Active Students.
Chief Instructor Leadership Level (Fire) will follow the same guidelines as 4 level concept as water. Just change out water for fire and change out
Blue for red.
For Lead Instructor Wind , its only 1 level
Should be a white hexagon with a black outline and black wind symbol.
Final one, earth should be on top because its the hardest to obtain leadership wise. Same 4 levels as water and fire but the leadership requirements are diffrent.
Level 1 for earth
200 Active Students and 3 Active instructors who've earned elements.
Level 2 for earth
350 Active Students and 6 Active instructors who've earned elements.
Level 3 for earth
500 Active Students and 9 Active instructors who've earned elements.
Level 4 for earth
1000 Active Students and 18 Active instructors who've earned elements.
Label the graphic design with
Kindle Lumo Pathway (on the bottom)
Serve Beyond Yourself (at the top)
Also i uploaded my belt posters so you dan gry to match the black/white/gold aethstetic. But please do elemental colored boxes like you did before in your previous design

```html
<!DOCTYPE html>
<html lang="en">
<head>
<meta charset="utf-8">
<title>Lumo Leadership Hierchy</title>
<link rel="stylesheet" href="https://fonts.googleapis.com/css2?family=Cinzel:wght@700;900&family=Lato:wght@400;900&family=Michroma&display=swap">
<style>
  :root {
    --backdrop: #b3b3b3;
    --ink: #000000;
    --paper: #ffffff;
    --gold: #e0b400;
    --earth: #138a33;
    --earth-deep: #0b7a26;
    --fire: #ff0000;
    --fire-deep: #e00000;
    --water: #003f6b;
    --silver: #b4b4b4;
    --edge: #2b2b2b;
  }
  * { box-sizing: border-box; margin: 0; padding: 0; }
  html, body { width: 913px; height: 1200px; overflow: hidden; background: var(--backdrop); }
  .canvas { position: relative; width: 913px; height: 1200px; font-family: "Lato", sans-serif; }
  .abs { position: absolute; }

  .poster { left: 81px; top: 83px; width: 751px; height: 1034px; background: var(--ink); }
  .gold-frame { left: 99px; top: 99px; width: 713px; height: 1004px; border: 3px solid var(--gold); }
  .corner { width: 38px; height: 38px; background: var(--gold); }
  .corner.tl { left: 99px; top: 99px; border-radius: 0 0 38px 0; }
  .corner.tr { left: 774px; top: 99px; border-radius: 0 0 0 38px; }
  .corner.bl { left: 99px; top: 1065px; border-radius: 0 38px 0 0; }
  .corner.br { left: 774px; top: 1065px; border-radius: 38px 0 0 0; }

  .panel { left: 102px; top: 213px; width: 707px; height: 850px; background: var(--paper); }
  .foot-band { left: 102px; top: 1060px; width: 707px; height: 43px; background: var(--gold); }

  .motto { left: 265px; top: 136px; width: 510px; color: var(--paper); font-family: "Cinzel", serif; font-weight: 900; font-size: 35px; line-height: 1; letter-spacing: -0.5px; white-space: nowrap; }
  .title-band { left: 120px; top: 190px; width: 669px; height: 49px; background: var(--gold); }
  .title { left: 265px; top: 196px; color: var(--ink); font-weight: 900; font-size: 35px; line-height: 1; white-space: nowrap; letter-spacing: 0.2px; }

  .brand-mark { left: 164px; top: 146px; width: 84px; height: 84px; border-radius: 50%; background: var(--ink); border: 4px solid var(--paper); display: flex; align-items: center; justify-content: center; }
  .brand-name { color: var(--paper); font-weight: 900; font-size: 19px; letter-spacing: 1px; }

  .rule-h { height: 2px; background: var(--gold); }
  .rule-v { width: 2px; background: var(--gold); }

  .tab { left: 331px; top: 260px; width: 246px; height: 28px; background: var(--gold); clip-path: polygon(0 0, 100% 0, 96% 100%, 4% 100%); display: flex; align-items: center; justify-content: center; }
  .tab-label { font-family: "Michroma", sans-serif; font-size: 19px; font-weight: 400; color: var(--ink); letter-spacing: 0.5px; -webkit-text-stroke: 0.8px var(--ink); }

  .step { width: 13px; height: 13px; border-radius: 50%; background: var(--gold); color: var(--paper); font-size: 7px; font-weight: 900; display: flex; align-items: center; justify-content: center; }

  .badge { width: 66px; height: 78px; }

  .req { line-height: 1; color: var(--ink); white-space: nowrap; }
  .req .big { font-weight: 900; font-size: 15.5px; display: block; }
  .req .small { font-weight: 400; font-size: 15.5px; display: block; margin-top: 1px; }
  .req .line { display: block; height: 16px; }

  .count { color: var(--ink); font-weight: 900; line-height: 0.92; white-space: nowrap; }
  .count .top { display: block; font-size: 17.5px; }
  .count .bottom { display: block; font-size: 22px; letter-spacing: 0.3px; }

  .role-bar { color: var(--paper); font-weight: 900; font-size: 24px; line-height: 1.05; }
  .lead-bar { left: 122px; top: 537px; width: 374px; height: 41px; background: var(--ink); display: flex; align-items: center; padding-left: 125px; }
  .chief-bar { left: 122px; top: 686px; width: 174px; height: 68px; background: var(--fire); padding: 9px 0 0 16px; }
  .director-bar { left: 122px; top: 884px; width: 174px; height: 69px; background: var(--water); padding: 9px 0 0 19px; }

  .closing { left: 122px; top: 1016px; width: 665px; height: 52px; background: var(--ink); display: flex; align-items: center; justify-content: center; }
  .closing-text { color: var(--paper); font-family: "Cinzel", serif; font-weight: 900; font-size: 33px; letter-spacing: 1px; }

  .earth-1 { --base: var(--earth); --rim: var(--paper); }
  .earth-2 { --base: var(--earth-deep); --rim: var(--ink); }
  .earth-3, .earth-4 { --base: var(--earth); --rim: var(--silver); }
  .wind { --base: var(--paper); --rim: var(--ink); }
  .fire-1 { --base: var(--fire); --rim: var(--paper); }
  .fire-2 { --base: var(--fire-deep); --rim: var(--ink); }
  .fire-3, .fire-4 { --base: var(--fire); --rim: var(--silver); }
  .water-1 { --base: var(--water); --rim: var(--paper); }
  .water-2 { --base: var(--water); --rim: var(--ink); }
  .water-3, .water-4 { --base: var(--water); --rim: var(--silver); }
</style>
</head>
<body>
<svg width="0" height="0" style="position:absolute">
  <defs>
    <symbol id="element-badge" viewBox="0 0 66 78">
      <polygon points="33,1 65,19.5 65,58.5 33,77 1,58.5 1,19.5" fill="var(--rim)" stroke="var(--edge)" stroke-width="1"/>
      <polygon points="33,5 61.5,21.5 61.5,56.5 33,73 4.5,56.5 4.5,21.5" fill="var(--base)"/>
      <circle cx="33" cy="39" r="20" fill="none" stroke="var(--rim)" stroke-width="3"/>
    </symbol>
  </defs>
</svg>

<main class="canvas">
  <div class="abs poster"></div>
  <div class="abs gold-frame"></div>
  <div class="abs corner tl"></div>
  <div class="abs corner tr"></div>
  <div class="abs corner bl"></div>
  <div class="abs corner br"></div>
  <div class="abs panel"></div>
  <div class="abs foot-band"></div>

  <h1 class="abs motto">SERVE BEYOND YOURSELF</h1>
  <div class="abs title-band"></div>
  <h2 class="abs title">LUMO LEADERSHIP HIERCHY</h2>
  <div class="abs brand-mark"><span class="brand-name">LUMO</span></div>

  <!-- Grand level -->
  <div class="abs rule-h" style="left:122px;top:259px;width:665px;"></div>
  <div class="abs rule-h" style="left:122px;top:495px;width:665px;"></div>
  <div class="abs rule-v" style="left:146px;top:260px;height:236px;"></div>
  <div class="abs rule-v" style="left:470px;top:288px;height:208px;"></div>
  <div class="abs tab"><span class="tab-label">GRAND LEVEL</span></div>

  <div class="abs step" style="left:141px;top:344px;">1</div>
  <div class="abs step" style="left:141px;top:429px;">2</div>
  <div class="abs step" style="left:465px;top:344px;">3</div>
  <div class="abs step" style="left:465px;top:429px;">4</div>

  <svg class="abs badge earth-1" style="left:170px;top:311px;" role="img" aria-label="Earth element symbol, level 1"><use href="#element-badge"/></svg>
  <svg class="abs badge earth-2" style="left:170px;top:396px;" role="img" aria-label="Earth element symbol, level 2"><use href="#element-badge"/></svg>
  <svg class="abs badge earth-3" style="left:501px;top:311px;" role="img" aria-label="Earth element symbol, level 3"><use href="#element-badge"/></svg>
  <svg class="abs badge earth-4" style="left:501px;top:402px;" role="img" aria-label="Earth element symbol, level 4"><use href="#element-badge"/></svg>

  <p class="abs req" style="left:246px;top:326px;"><span class="big line">200 ACTIVE STUDENTS</span><span class="big line">&amp; 3 ACTIVE INSTRUCTORS</span><span class="small">who've earned elements.</span></p>
  <p class="abs req" style="left:246px;top:412px;"><span class="big line">350 ACTIVE STUDENTS</span><span class="big line">&amp; 6 ACTIVE INSTRUCTORS</span><span class="small">who've earned elements.</span></p>
  <p class="abs req" style="left:579px;top:326px;"><span class="big line">500 ACTIVE STUDENTS</span><span class="big line">&amp; 9 ACTIVE INSTRUCTORS</span><span class="small">who've earned elements.</span></p>
  <p class="abs req" style="left:579px;top:412px;"><span class="big line">1000 ACTIVE STUDENTS</span><span class="big line">&amp; 18 ACTIVE INSTRUCTORS</span><span class="small">who've earned elements.</span></p>

  <!-- Lead instructor -->
  <div class="abs lead-bar role-bar">LEAD INSTRUCTOR</div>
  <svg class="abs badge wind" style="left:495px;top:518px;width:66px;height:80px;" role="img" aria-label="Wind element symbol"><use href="#element-badge"/></svg>
  <p class="abs count" style="left:569px;top:539px;"><span class="top">50 ACTIVE</span><span class="bottom">STUDENTS</span></p>
  <div class="abs rule-h" style="left:122px;top:617px;width:665px;"></div>

  <!-- Chief instructor -->
  <div class="abs rule-v" style="left:296px;top:618px;height:206px;"></div>
  <div class="abs rule-v" style="left:541px;top:618px;height:206px;"></div>
  <div class="abs chief-bar role-bar">CHIEF<br>INSTRUCTOR</div>
  <div class="abs step" style="left:290px;top:670px;">1</div>
  <div class="abs step" style="left:290px;top:756px;">2</div>
  <div class="abs step" style="left:536px;top:670px;">3</div>
  <div class="abs step" style="left:536px;top:756px;">4</div>
  <svg class="abs badge fire-1" style="left:320px;top:638px;" role="img" aria-label="Fire element symbol, level 1"><use href="#element-badge"/></svg>
  <svg class="abs badge fire-2" style="left:320px;top:724px;" role="img" aria-label="Fire element symbol, level 2"><use href="#element-badge"/></svg>
  <svg class="abs badge fire-3" style="left:572px;top:638px;" role="img" aria-label="Fire element symbol, level 3"><use href="#element-badge"/></svg>
  <svg class="abs badge fire-4" style="left:572px;top:729px;" role="img" aria-label="Fire element symbol, level 4"><use href="#element-badge"/></svg>
  <p class="abs count" style="left:394px;top:661px;"><span class="top">50 ACTIVE</span><span class="bottom">STUDENTS</span></p>
  <p class="abs count" style="left:394px;top:746px;"><span class="top">100 ACTIVE</span><span class="bottom">STUDENTS</span></p>
  <p class="abs count" style="left:648px;top:661px;"><span class="top">150 ACTIVE</span><span class="bottom">STUDENTS</span></p>
  <p class="abs count" style="left:648px;top:746px;"><span class="top">200 ACTIVE</span><span class="bottom">STUDENTS</span></p>
  <div class="abs rule-h" style="left:122px;top:823px;width:665px;"></div>

  <!-- Program director -->
  <div class="abs rule-v" style="left:296px;top:824px;height:192px;"></div>
  <div class="abs rule-v" style="left:541px;top:824px;height:192px;"></div>
  <div class="abs director-bar role-bar">PROGRAM<br>DIRECTOR</div>
  <div class="abs step" style="left:290px;top:868px;">1</div>
  <div class="abs step" style="left:290px;top:954px;">2</div>
  <div class="abs step" style="left:536px;top:868px;">3</div>
  <div class="abs step" style="left:536px;top:954px;">4</div>
  <svg class="abs badge water-1" style="left:320px;top:836px;" role="img" aria-label="Water element symbol, level 1"><use href="#element-badge"/></svg>
  <svg class="abs badge water-2" style="left:320px;top:922px;" role="img" aria-label="Water element symbol, level 2"><use href="#element-badge"/></svg>
  <svg class="abs badge water-3" style="left:572px;top:836px;" role="img" aria-label="Water element symbol, level 3"><use href="#element-badge"/></svg>
  <svg class="abs badge water-4" style="left:572px;top:927px;" role="img" aria-label="Water element symbol, level 4"><use href="#element-badge"/></svg>
  <p class="abs count" style="left:394px;top:859px;"><span class="top">50 ACTIVE</span><span class="bottom">STUDENTS</span></p>
  <p class="abs count" style="left:394px;top:944px;"><span class="top">100 ACTIVE</span><span class="bottom">STUDENTS</span></p>
  <p class="abs count" style="left:648px;top:859px;"><span class="top">150 ACTIVE</span><span class="bottom">STUDENTS</span></p>
  <p class="abs count" style="left:648px;top:944px;"><span class="top">200 ACTIVE</span><span class="bottom">STUDENTS</span></p>

  <footer class="abs closing"><span class="closing-text">KINDLE LUMO PATHWAY</span></footer>
</main>
</body>
</html>
```